Calendar Dates Only

Need monthly 2018 calendar showing Australian holidays. Need 2 versions 1 black and white and one with some colour. Also need calendar with week starting on Mondays and also on Sundays. Prefer Indesign versions so text can be changed if necessary. Dates only required which would be A4 landscape format. May also need portrait format.

Colors

```html
<!DOCTYPE html>
<html lang="en">
<head>
<meta charset="utf-8">
<title>Calendar 2018 — January to April</title>
<link href="https://fonts.googleapis.com/css2?family=Oswald:wght@300;400&display=swap" rel="stylesheet">
<style>
  :root{
    --backdrop:#808080;
    --paper:#edeedb;
    --title:#5d5a2b;
    --number:#867637;
    --weekday:#958d73;
    --rule:#9c8e72;
    --holiday:#ddd4be;
    --holiday-soft:#e8dfc9;
    --label:#4d4526;
    --footer-band:#e6b797;
  }
  *{box-sizing:border-box;margin:0;padding:0}
  html,body{width:1200px;height:1175px;overflow:hidden}
  body{background:var(--backdrop);position:relative;font-family:'Oswald',sans-serif}
  .sheet{position:absolute;left:12px;top:98px;width:1172px;height:954px;background:var(--paper)}
  .sheet-band{position:absolute;left:0;right:0;bottom:2px;height:16px;background:var(--footer-band)}
  .month{position:absolute;width:503px}
  .month-title{position:absolute;left:0;width:100%;text-align:center;font-weight:400;font-size:36px;color:var(--title);letter-spacing:.5px;line-height:1}
  .weekdays{position:absolute;left:0;width:100%;display:grid;grid-template-columns:repeat(7,1fr);font-weight:300;font-size:12.5px;color:var(--weekday);text-align:center;text-transform:uppercase}
  .days{position:absolute;left:0;width:100%;display:grid;grid-template-columns:repeat(7,1fr);grid-auto-rows:54px;border-left:1px solid var(--rule);border-top:1px solid var(--rule)}
  .day{position:relative;border-right:1px solid var(--rule);border-bottom:1px solid var(--rule)}
  .day b{position:absolute;right:7px;top:15px;font-weight:300;font-size:18px;color:var(--number);line-height:1}
  .day.holiday{background:var(--holiday)}
  .day.holiday-soft{background:var(--holiday-soft)}
  .day small{position:absolute;left:3px;bottom:4px;font-size:7px;color:var(--label);font-weight:400;white-space:nowrap;font-family:'Arial Narrow',sans-serif}
  .jan{left:37px;top:0} .feb{left:598px;top:0}
  .mar{left:37px;top:0} .apr{left:598px;top:0}
  .top .month-title{top:50px} .top .weekdays{top:130px} .top .days{top:156px}
  .mar .month-title{top:476px} .mar .weekdays{top:548px} .mar .days{top:575px}
  .apr .month-title{top:476px} .apr .weekdays{top:546px} .apr .days{top:573px}
</style>
</head>
<body>
<main class="sheet">

  <section class="month jan top">
    <h2 class="month-title">JANUARY 2018</h2>
    <div class="weekdays"><span>Monday</span><span>Tuesday</span><span>Wednesday</span><span>Thursday</span><span>Friday</span><span>Saturday</span><span>Sunday</span></div>
    <div class="days">
      <div class="day holiday"><b>1</b><small>New Year's Day</small></div><div class="day"><b>2</b></div><div class="day"><b>3</b></div><div class="day"><b>4</b></div><div class="day"><b>5</b></div><div class="day"><b>6</b></div><div class="day"><b>7</b></div>
      <div class="day"><b>8</b></div><div class="day"><b>9</b></div><div class="day"><b>10</b></div><div class="day"><b>11</b></div><div class="day"><b>12</b></div><div class="day"><b>13</b></div><div class="day"><b>14</b></div>
      <div class="day"><b>15</b></div><div class="day"><b>16</b></div><div class="day"><b>17</b></div><div class="day"><b>18</b></div><div class="day"><b>19</b></div><div class="day"><b>20</b></div><div class="day"><b>21</b></div>
      <div class="day"><b>22</b></div><div class="day"><b>23</b></div><div class="day"><b>24</b></div><div class="day"><b>25</b></div><div class="day holiday"><b>26</b><small>Australia day</small></div><div class="day"><b>27</b></div><div class="day"><b>28</b></div>
      <div class="day"><b>29</b></div><div class="day"><b>30</b></div><div class="day"><b>31</b></div><div class="day"></div><div class="day"></div><div class="day"></div><div class="day"></div>
    </div>
  </section>

  <section class="month feb top">
    <h2 class="month-title">FEBRUARY 2018</h2>
    <div class="weekdays"><span>Monday</span><span>Tuesday</span><span>Wednesday</span><span>Thursday</span><span>Friday</span><span>Saturday</span><span>Sunday</span></div>
    <div class="days">
      <div class="day"></div><div class="day"></div><div class="day"></div><div class="day"><b>1</b></div><div class="day"><b>2</b></div><div class="day"><b>3</b></div><div class="day"><b>4</b></div>
      <div class="day"><b>5</b></div><div class="day"><b>6</b></div><div class="day"><b>7</b></div><div class="day"><b>8</b></div><div class="day"><b>9</b></div><div class="day"><b>10</b></div><div class="day"><b>11</b></div>
      <div class="day"><b>12</b></div><div class="day"><b>13</b></div><div class="day"><b>14</b></div><div class="day"><b>15</b></div><div class="day"><b>16</b></div><div class="day"><b>17</b></div><div class="day"><b>18</b></div>
      <div class="day"><b>19</b></div><div class="day"><b>20</b></div><div class="day"><b>21</b></div><div class="day"><b>22</b></div><div class="day"><b>23</b></div><div class="day"><b>24</b></div><div class="day"><b>25</b></div>
      <div class="day"><b>26</b></div><div class="day"><b>27</b></div><div class="day"><b>28</b></div><div class="day"></div><div class="day"></div><div class="day"></div><div class="day"></div>
    </div>
  </section>

  <section class="month mar">
    <h2 class="month-title">MARCH 2018</h2>
    <div class="weekdays"><span>Monday</span><span>Tuesday</span><span>Wednesday</span><span>Thursday</span><span>Friday</span><span>Saturday</span><span>Sunday</span></div>
    <div class="days">
      <div class="day"></div><div class="day"></div><div class="day"></div><div class="day"><b>1</b></div><div class="day"><b>2</b></div><div class="day"><b>3</b></div><div class="day"><b>4</b></div>
      <div class="day holiday"><b>5</b><small>Labour day</small></div><div class="day"><b>6</b></div><div class="day"><b>7</b></div><div class="day"><b>8</b></div><div class="day"><b>9</b></div><div class="day"><b>10</b></div><div class="day"><b>11</b></div>
      <div class="day holiday"><b>12</b><small>Canberra day</small></div><div class="day"><b>13</b></div><div class="day"><b>14</b></div><div class="day"><b>15</b></div><div class="day"><b>16</b></div><div class="day"><b>17</b></div><div class="day"><b>18</b></div>
      <div class="day"><b>19</b></div><div class="day"><b>20</b></div><div class="day"><b>21</b></div><div class="day"><b>22</b></div><div class="day"><b>23</b></div><div class="day"><b>24</b></div><div class="day"><b>25</b></div>
      <div class="day"><b>26</b></div><div class="day"><b>27</b></div><div class="day"><b>28</b></div><div class="day"><b>29</b></div><div class="day holiday"><b>30</b><small>Good Friday</small></div><div class="day holiday"><b>31</b><small>Easter Saturday</small></div><div class="day"></div>
    </div>
  </section>

  <section class="month apr">
    <h2 class="month-title">APRIL 2018</h2>
    <div class="weekdays"><span>Monday</span><span>Tuesday</span><span>Wednesday</span><span>Thursday</span><span>Friday</span><span>Saturday</span><span>Sunday</span></div>
    <div class="days">
      <div class="day"></div><div class="day"></div><div class="day"></div><div class="day"></div><div class="day"></div><div class="day"></div><div class="day holiday"><b>1</b><small>Easter Sunday</small></div>
      <div class="day holiday-soft"><b>2</b><small>Easter Monday</small></div><div class="day holiday-soft"><b>3</b><small>Easter Tuesday</small></div><div class="day"><b>4</b></div><div class="day"><b>5</b></div><div class="day"><b>6</b></div><div class="day"><b>7</b></div><div class="day"><b>8</b></div>
      <div class="day"><b>9</b></div><div class="day"><b>10</b></div><div class="day"><b>11</b></div><div class="day"><b>12</b></div><div class="day"><b>13</b></div><div class="day"><b>14</b></div><div class="day"><b>15</b></div>
      <div class="day"><b>16</b></div><div class="day"><b>17</b></div><div class="day"><b>18</b></div><div class="day"><b>19</b></div><div class="day"><b>20</b></div><div class="day"><b>21</b></div><div class="day"><b>22</b></div>
      <div class="day"><b>23</b></div><div class="day"><b>24</b></div><div class="day holiday"><b>25</b><small>Anzac day</small></div><div class="day"><b>26</b></div><div class="day"><b>27</b></div><div class="day"><b>28</b></div><div class="day"><b>29</b></div>
      <div class="day"><b>30</b></div><div class="day"></div><div class="day"></div><div class="day"></div><div class="day"></div><div class="day"></div><div class="day"></div>
    </div>
  </section>

  <div class="sheet-band"></div>
</main>
</body>
</html>
```